Business card design needed

Family General Practitioner/ Family Physician.
Logo is the logo of the Crestmoor Guild of Family Clinicians Australia
http://kvplm.tarevo.edu.au/PictureGallery/logos/pages/CGFC%20logo_jpg.htm

Reason: Just a bit more time to make changes and the weekend for me to look at things closely and to choose. Thanks, Lumi

Thanks for all the submissions. So many of them are really works of art. Not one of them are not good. The ones that I am eliminating are the ones that I think are not suitable for me personally only, and because if I don't, it makes it very difficult to decide as many of you are also sending me slight variations of a card. I have just decided to choose a second place card too. Can't thank you all enough. Good luck, Lumi. P.S - Working today till 10 pm as the card says :-), so probably won't be able to give a feedback till late Saturday night or Sunday morning here in Sydney, Australia. 

Reason: Just added a second place to the budget and realised that Australia is ahead of the rest of the world in the time zone (only :-) - don't want to offend anyone or start a debate!! ) , so Monday deadline will mean it will be a weekend for the rest of the world. Just wanted to give everyone more time to submit their best, especially since I will be picking a second card too. Can't thank everyone enough for the submissions. P.S - Not keen on photos on the card.

Contact Information for Business Card

Dr. Lumi Harcourt M.B.B.S., F.C.G.F.C
Family General Practitioner
Address, timings, phone and fax number on the back.

Requirements
Must have
• Timings
Mon 7 am - 7 pm
Tues 7 am - 12 pm
Wed 7 am - 10 pm
Thurs 7 am - 12 pm
Fri 7 am - 8 pm
Sat 8 am - 10 pm
Sun - Off

```html
<!DOCTYPE html>
<html lang="en">
<head>
<meta charset="utf-8">
<title>Dr. Lumi Harcourt – Business Card</title>
<link rel="stylesheet" href="https://fonts.googleapis.com/css2?family=Open+Sans:wght@400;600;700&family=Cinzel:wght@400;600&family=Dancing+Script:wght@500&display=swap">
<style>
  :root {
    --backdrop: #2a2a2a;
    --card-white: #fbfbfb;
    --ink: #1a1a1a;
    --accent-red: #c0182c;
    --teal-light: #21769b;
    --teal-mid: #145271;
    --teal-dark: #0a2536;
    --front-text: #f4f6f8;
  }
  * { margin: 0; padding: 0; box-sizing: border-box; }
  html, body {
    width: 1200px;
    height: 949px;
    overflow: hidden;
    background: var(--backdrop);
  }
  .stage {
    position: relative;
    width: 1200px;
    height: 949px;
  }
  .card {
    position: absolute;
    top: 325px;
    width: 520px;
    height: 300px;
    border-radius: 16px;
    overflow: hidden;
    box-shadow: 0 10px 30px rgba(0,0,0,0.5);
  }

  /* Back side: timings and contact */
  .card-back {
    left: 60px;
    background: var(--card-white);
    font-family: "Open Sans", Arial, sans-serif;
    color: var(--ink);
  }
  .timings-label {
    position: absolute;
    left: 46px;
    top: 46px;
    width: 106px;
    height: 76px;
    background: var(--accent-red);
    color: #fff;
    font-weight: 600;
    font-size: 19px;
    line-height: 24px;
    padding: 0 0 8px 12px;
    display: flex;
    align-items: flex-end;
  }
  .contact-lines {
    position: absolute;
    left: 166px;
    top: 42px;
    font-size: 19px;
    line-height: 27px;
  }
  .schedule {
    position: absolute;
    left: 72px;
    top: 132px;
    border-collapse: collapse;
    font-size: 15px;
    line-height: 19px;
  }
  .schedule th {
    font-weight: 400;
    text-align: left;
    width: 66px;
    padding: 0;
  }
  .schedule td { white-space: nowrap; padding: 0; }
  .closed-day {
    position: absolute;
    left: 72px;
    top: 250px;
    color: var(--accent-red);
    font-weight: 700;
    font-size: 21px;
    line-height: 26px;
  }

  /* Front side: name and credentials */
  .card-front {
    left: 620px;
    background: radial-gradient(ellipse 75% 80% at 40% 40%, var(--teal-light) 0%, var(--teal-mid) 50%, var(--teal-dark) 100%);
    color: var(--front-text);
  }
  .tagline {
    position: absolute;
    left: 52px;
    top: 42px;
    font-family: "Dancing Script", cursive;
    font-size: 22px;
    line-height: 28px;
  }
  .guild-mark {
    position: absolute;
    right: 40px;
    top: 62px;
    font-family: "Cinzel", serif;
    font-weight: 600;
    font-size: 26px;
    line-height: 32px;
    letter-spacing: 2px;
    color: var(--front-text);
  }
  .accent-block {
    position: absolute;
    left: 0;
    top: 160px;
    width: 52px;
    height: 60px;
    background: var(--accent-red);
  }
  .identity {
    position: absolute;
    left: 63px;
    top: 164px;
    font-family: "Cinzel", serif;
  }
  .doctor-name {
    font-size: 21px;
    font-weight: 600;
    line-height: 24px;
  }
  .credentials {
    font-size: 13px;
    padding-left: 4px;
    line-height: 18px;
    letter-spacing: 0.5px;
  }
  .role {
    font-size: 12px;
    font-weight: 600;
    line-height: 16px;
    letter-spacing: 0.3px;
  }
</style>
</head>
<body>
<main class="stage">
  <section class="card card-back" aria-label="Card back: timings and contact">
    <div class="timings-label">Timings:</div>
    <div class="contact-lines">
      <p>phone: 00 000000</p>
      <p>fax: 00 000000</p>
    </div>
    <table class="schedule">
      <tr><th>Mon</th><td>7 am - 7 pm</td></tr>
      <tr><th>Tues</th><td>7 am - 12 pm</td></tr>
      <tr><th>Wed</th><td>7 am - 10 pm</td></tr>
      <tr><th>Thurs</th><td>7 am - 12 pm</td></tr>
      <tr><th>Fri</th><td>7 am - 8 pm</td></tr>
      <tr><th>Sat</th><td>8 am - 10 pm</td></tr>
    </table>
    <p class="closed-day">Sun - Off</p>
  </section>

  <section class="card card-front" aria-label="Card front: doctor identity">
    <p class="tagline">"Caring about your health"</p>
    <p class="guild-mark">CGFC</p>
    <div class="accent-block"></div>
    <div class="identity">
      <h1 class="doctor-name">Dr. Lumi Harcourt</h1>
      <p class="credentials">M.B.B.S., F.C.G.F.C</p>
      <p class="role">Family General Practitioner</p>
    </div>
  </section>
</main>
</body>
</html>
```